Professional Services/Construction Management (Millwork) Biz Cards

We've decided on a logo and have our color palette set, now we want to design some very professional looking cards that make a strong first impression - they'll reflect our tagline (that we're going to put on the back: Innovative. Professional. Leaders.

The example business card shows generally the direction we've been thinking of going for the back side - **but we're open to other ideas**

Target Market(s)

The cards should target more high-end (wealthy) owners and general contracting companies. We want them to convey a strong first impression - in a professional and not garish way.

Industry/Entity Type

Construction Company

Contact Information for Business Card

There needs to be a place for our company contractor's license number and business address. We want to also have people's names, titles, phone number, email address. The back can be the logo, tagline and web address

Requirements
Must have
• follow our color palette
Nice to have
• Font & Styles should compliment the Harrow Joinery fonts, but not necessarily match exactly

```html
<!DOCTYPE html>
<html lang="en">
<head>
<meta charset="utf-8">
<title>Harrow Joinery Business Cards</title>
<link href="https://fonts.googleapis.com/css2?family=Open+Sans:wght@400;600;700;800&display=swap" rel="stylesheet">
<style>
  :root {
    --bg: #2a2a2a;
    --brown: #5e4c3e;
    --brown-dark: #4a3b30;
    --green: #5aa443;
    --white: #ffffff;
    --ink: #3f3127;
    --muted: #6b5d52;
  }
  * { margin: 0; padding: 0; box-sizing: border-box; }
  html, body {
    width: 1200px; height: 900px; overflow: hidden;
    background: var(--bg);
    font-family: "Open Sans", Arial, sans-serif;
  }
  .canvas { position: relative; width: 1200px; height: 900px; }
  .card {
    position: absolute; left: 290px;
    width: 620px; height: 354px;
    border-radius: 22px;
    overflow: hidden;
  }
  /* Back side */
  .card-back { top: 70px; background: var(--brown); color: var(--white); }
  .back-mark {
    position: absolute; right: 70px; top: 46px;
    display: flex; flex-direction: column; align-items: center; gap: 16px;
  }
  .back-mark .dot {
    width: 150px; height: 150px; border-radius: 50%;
    background: var(--green);
  }
  .brand-name {
    font-weight: 700; font-size: 26px; letter-spacing: 0.5px;
  }
  .card-back .brand-name { color: var(--white); }
  .tagline {
    position: absolute; left: 40px; bottom: 52px;
    font-size: 14px; letter-spacing: 0.6px; text-transform: uppercase;
  }
  .website {
    position: absolute; right: 40px; bottom: 52px;
    font-size: 14px; letter-spacing: 0.3px;
  }
  /* Front side */
  .card-front { top: 476px; background: var(--white); color: var(--ink); }
  .front-mark {
    position: absolute; left: 36px; top: 70px;
    display: flex; flex-direction: column; align-items: center; gap: 12px;
  }
  .front-mark .dot {
    width: 130px; height: 130px; border-radius: 50%;
    background: var(--brown);
  }
  .card-front .brand-name { color: var(--brown); font-size: 22px; }
  .contact {
    position: absolute; right: 40px; top: 34px;
    text-align: right;
  }
  .person-name { font-weight: 800; font-size: 28px; color: var(--ink); line-height: 1.1; }
  .person-title { font-weight: 600; font-size: 14px; color: var(--green); margin-bottom: 10px; }
  .address { font-size: 14px; color: var(--muted); line-height: 1.45; }
  .divider {
    height: 2px; background: var(--green); width: 190px;
    margin: 8px 0 8px auto;
  }
  .contact-line {
    display: flex; justify-content: flex-end; align-items: center; gap: 8px;
    font-size: 14px; color: var(--muted); line-height: 1.6;
  }
  .contact-line svg { width: 12px; height: 12px; flex: none; }
  .rule {
    position: absolute; left: 40px; right: 0; bottom: 62px;
    height: 2px; background: var(--green);
  }
  .license {
    position: absolute; left: 40px; bottom: 28px;
    font-size: 14px; color: var(--muted); letter-spacing: 0.3px;
  }
</style>
</head>
<body>
<main class="canvas">
  <section class="card card-back" aria-label="Card back">
    <div class="back-mark">
      <div class="dot"></div>
      <span class="brand-name">Harrow Joinery</span>
    </div>
    <p class="tagline">Innovative. Professional. Leaders.</p>
    <p class="website">www.harrowjoinery.com</p>
  </section>

  <section class="card card-front" aria-label="Card front">
    <div class="front-mark">
      <div class="dot"></div>
      <span class="brand-name">Harrow Joinery</span>
    </div>
    <div class="contact">
      <p class="person-name">Owen Marsh</p>
      <p class="person-title">President</p>
      <p class="address">482 Ridge Avenue<br>Millbrook, OH 44390</p>
      <div class="divider"></div>
      <p class="contact-line">330-555-0187
        <svg viewBox="0 0 24 24" aria-hidden="true"><path fill="#5aa443" d="M6.6 10.8a15.1 15.1 0 0 0 6.6 6.6l2.2-2.2a1 1 0 0 1 1-.25 11.4 11.4 0 0 0 3.6.57 1 1 0 0 1 1 1V20a1 1 0 0 1-1 1A17 17 0 0 1 3 4a1 1 0 0 1 1-1h3.5a1 1 0 0 1 1 1c0 1.25.2 2.45.57 3.57a1 1 0 0 1-.25 1z"/></svg>
      </p>
      <p class="contact-line">omarsh@harrowjoinery.com
        <svg viewBox="0 0 24 24" aria-hidden="true"><rect x="2" y="5" width="20" height="14" rx="2" fill="none" stroke="#5aa443" stroke-width="2.4"/><path d="M3 6l9 7 9-7" fill="none" stroke="#5aa443" stroke-width="2.4"/></svg>
      </p>
    </div>
    <div class="rule"></div>
    <p class="license">NV Lic. #40736</p>
  </section>
</main>
</body>
</html>
```